Trifold brochure

Please design a new trifold color brochure. I've uploaded our very outdated brochure for info purposes. I've uploaded some pictures of some items we've made as examples. Use stock photos or our photos, your preference. Use our new logo that is attached.

```html
<!DOCTYPE html>
<html lang="en">
<head>
<meta charset="utf-8">
<title>Halden Steelworks – Trifold Brochure</title>
<link href="https://fonts.googleapis.com/css2?family=Lexend:wght@300;400;600&family=Oswald:wght@500&family=Krona+One&display=swap" rel="stylesheet">
<style>
:root{
  --navy:#1f3f8f;
  --navy-deep:#1a3a86;
  --royal:#2452b5;
  --bright:#0b72c0;
  --silver-hi:#f4f5f7;
  --silver-mid:#c9ccd2;
  --silver-lo:#9a9ea6;
  --ink:#2a2d33;
  --white:#ffffff;
  --page:#f2f2f2;
}
*{margin:0;padding:0;box-sizing:border-box}
html,body{width:1200px;height:2414px;overflow:hidden;background:var(--page)}
body{position:relative;font-family:"Lexend",sans-serif;color:var(--ink)}
.spread{position:absolute;left:30px;width:1033px;height:735px;transform:scale(1.1036);transform-origin:top left;overflow:hidden;box-shadow:0 4px 18px rgba(0,0,0,.12)}
.spread--outside{top:376px}
.spread--inside{top:1227px;background:linear-gradient(120deg,var(--silver-lo) 0%,var(--silver-hi) 28%,var(--silver-mid) 50%,var(--silver-hi) 72%,var(--silver-lo) 100%)}
.panel{position:absolute;top:0;height:735px}
.silver{background:linear-gradient(90deg,var(--silver-lo),var(--silver-hi) 50%,var(--silver-lo))}
.photo{position:absolute}
.brand{position:absolute;display:flex;align-items:center;gap:8px;font-family:"Lexend",sans-serif;font-weight:400;letter-spacing:.5px;white-space:nowrap}
.brand__mark{display:inline-block;flex:none;background:currentColor}
.brand--navy{color:var(--navy)}
.brand--white{color:var(--white)}

/* outside: back flap */
.flap{left:0;width:344px;background:var(--navy)}
.flap__head{position:absolute;left:0;top:0;width:344px;height:93px}
.flap__head .brand{left:44px;top:42px;font-size:12px;line-height:12px}
.flap__head .brand__mark{width:12px;height:12px}
.flap__tag{position:absolute;left:190px;top:42px;font-weight:600;font-size:12.5px;line-height:15px;color:var(--royal)}
.band{position:absolute;background:var(--bright)}

/* outside: middle */
.mailer{left:344px;width:337px;background:var(--navy)}
.mailer .brand{left:0;right:0;justify-content:center;top:92px;font-size:20px}
.mailer .brand__mark{width:18px;height:18px}
.address{position:absolute;left:0;right:0;top:530px;text-align:center;color:var(--white);font-size:12px;line-height:17px;font-weight:300}
.address strong{font-weight:600;font-size:13.5px}
.social{position:absolute;left:0;right:0;top:630px;display:flex;justify-content:center;gap:14px}
.social span{width:18px;height:18px;border-radius:50%;background:var(--white);opacity:.9}

/* outside: cover */
.cover{left:681px;width:352px}
.cover .brand{left:0;right:0;justify-content:center;top:86px;font-size:24px}
.cover .brand__mark{width:20px;height:20px}
.cover__kicker{position:absolute;left:0;right:0;text-align:center;font-size:17px;font-weight:300;color:var(--ink);letter-spacing:.5px}
.cover__title{position:absolute;left:0;right:0;top:188px;text-align:center;font-family:"Krona One",sans-serif;font-size:40px;color:var(--royal)}
.values{position:absolute;left:0;top:318px;width:352px;height:37px;background:var(--navy-deep);display:flex;justify-content:center;align-items:center;gap:14px;font-family:"Oswald",sans-serif;font-size:15px;color:var(--white);letter-spacing:.3px}
.cover__url{position:absolute;left:0;right:0;top:694px;text-align:center;font-size:15px;color:var(--royal)}
.cover__foot{position:absolute;left:0;bottom:0;width:352px;height:9px;background:var(--navy)}

/* inside */
.tab{position:absolute;top:50px;height:34px;width:168px;color:var(--white);font-size:13.5px;padding:8px 0 0 14px;background:var(--royal);clip-path:polygon(0 0,82% 0,100% 100%,0 100%)}
.mission{position:absolute;left:50px;top:104px;font-size:15.5px;line-height:26.5px;font-weight:300;color:var(--ink);white-space:nowrap}
.mission strong{font-weight:600}
.intro{position:absolute;font-size:11px;line-height:15px;font-weight:300;color:var(--ink);white-space:nowrap}
.products{position:absolute;left:398px;top:170px;width:243px;border-collapse:collapse;font-size:11.5px;font-weight:300}
.products td{height:29px;border-bottom:1.5px solid #3a3d44;padding:0 0 0 10px;width:50%;vertical-align:middle}
.contact{position:absolute;left:731px;top:278px;width:235px}
.contact h3{font-size:16px;font-weight:600;color:var(--navy);margin-bottom:6px}
.contact p{display:flex;align-items:center;gap:6px;font-size:11.5px;font-weight:300;color:var(--ink);height:24px;border-bottom:1px solid rgba(42,45,51,.45);white-space:nowrap}
.contact p:last-child{border-bottom:none}
.contact svg{width:9px;height:9px;fill:var(--ink);flex:none}
.hexart{position:absolute}
</style>
</head>
<body>

<!-- Outside spread -->
<section class="spread spread--outside">
  <div class="panel flap">
    <div class="flap__head silver">
      <div class="brand brand--navy"><span class="brand__mark"></span><span>HALDEN<br>STEELWORKS</span></div>
      <div class="flap__tag">Custom Metal<br>Fabrication</div>
    </div>
    <div class="band" style="left:0;top:238px;width:110px;height:92px"></div>
    <div class="band" style="left:215px;top:388px;width:129px;height:92px"></div>
    <div class="band" style="left:0;top:575px;width:80px;height:90px"></div>
    <div class="photo" role="img" aria-label="Fabricated dust collector vessel with gauges" style="left:72px;top:110px;width:136px;height:250px;background:linear-gradient(180deg,#9ea3aa,#3d3a3a);border-radius:6px"></div>
    <div class="photo" role="img" aria-label="White steel hopper on a support frame" style="left:72px;top:368px;width:160px;height:145px;background:linear-gradient(180deg,#f1f3f5,#d7dadf);border-radius:4px"></div>
    <div class="photo" role="img" aria-label="Stainless steel duct transition housing" style="left:70px;top:535px;width:180px;height:150px;background:linear-gradient(150deg,#d8dbd2,#9fa39a);border-radius:4px"></div>
  </div>

  <div class="panel mailer">
    <div class="brand brand--white"><span class="brand__mark"></span>HALDEN STEELWORKS</div>
    <div class="address">
      <strong>Halden Steelworks, Inc.</strong><br>
      2740 Orchard Rd. Fairview, VA 23000<br>
      Phone (555)-310-2284<br>
      www.haldensteelworks.com
    </div>
    <div class="social" aria-label="Social media links">
      <span></span><span></span><span></span>
    </div>
  </div>

  <div class="panel cover silver">
    <div class="brand brand--navy"><span class="brand__mark"></span>HALDEN STEELWORKS</div>
    <div class="cover__kicker" style="top:165px">Custom</div>
    <div class="cover__title">METAL</div>
    <div class="cover__kicker" style="top:243px">Fabrication</div>
    <div class="values"><span>QUALITY</span><span>DEPENDABILITY</span><span>INTEGRITY</span></div>
    <div class="photo" role="img" aria-label="Welder in protective gear welding a steel pipe with sparks in a factory" style="left:0;top:355px;width:352px;height:327px;background:linear-gradient(160deg,#c9d6e6,#5c7fae 45%,#1d3566)"></div>
    <div class="cover__url">www.haldensteelworks.com</div>
    <div class="cover__foot"></div>
  </div>
</section>

<!-- Inside spread -->
<section class="spread spread--inside">
  <div class="tab" style="left:50px">Our Mission</div>
  <div class="mission">We supply our customers<br><strong>fabricated metal products</strong><br>that are designed and<br>produced with the highest<br>quality, most competitive<br>pricing, and the fastest<br>lead-time<br>in the industry!</div>

  <svg class="hexart" style="left:0;top:310px" width="360" height="425" viewBox="0 0 360 425" aria-hidden="true">
    <polygon points="0,225 50,200 140,260 140,425 0,425" fill="var(--navy)"/>
    <polygon points="210,60 350,140 350,300 210,380 65,300 65,140" fill="var(--royal)"/>
  </svg>
  <svg class="hexart" style="left:82px;top:320px" width="258" height="290" viewBox="0 0 258 290">
    <polygon points="129,0 258,72 258,218 129,290 0,218 0,72" fill="#e3e5e8"/>
    <polygon points="129,14 244,79 244,211 129,276 14,211 14,79" fill="#7b8594" role="img" aria-label="Workers welding steel frames in a fabrication shop"/>
  </svg>

  <div class="tab" style="left:394px">Products</div>
  <p class="intro" style="left:394px;top:104px">Our products are as diverse as our customer<br>base. Some of the products we specialize<br>in are listed below…</p>
  <table class="products">
    <tr><td>Enclosures</td><td>Conveyors</td></tr>
    <tr><td>Platforms</td><td>Racks</td></tr>
    <tr><td>Stairs</td><td>Sheared Parts</td></tr>
    <tr><td>Guards</td><td>Welding</td></tr>
    <tr><td>Store Fixtures</td><td>Forming</td></tr>
    <tr><td>Baskets</td><td>Frames</td></tr>
    <tr><td>Pans</td><td>Modifications</td></tr>
    <tr><td>Duct Work</td><td>Channel</td></tr>
    <tr><td>Brackets</td><td>Panels</td></tr>
    <tr><td>Fittings</td><td>Cones</td></tr>
    <tr><td>Cladding</td><td>Discs</td></tr>
    <tr><td>Oxidizers</td><td>Shims</td></tr>
    <tr><td>Mixers</td><td>Covers</td></tr>
    <tr><td>Hoppers</td><td>Angles</td></tr>
    <tr><td>Ramps</td><td>Rails</td></tr>
    <tr><td>Carts</td><td>Clips</td></tr>
    <tr><td>Dryers</td><td>Transitions</td></tr>
  </table>

  <div class="tab" style="left:731px">Contacts</div>
  <p class="intro" style="left:731px;top:104px">Our project managers have spent many<br>years in the metal fabrication business.<br>They are very knowledgeable and have vast<br>experience in designing and producing items<br>for different types of industries.</p>
  <p class="intro" style="left:731px;top:200px">Give them a call today and see how<br>they can help you!</p>
  <div class="contact">
    <h3>Halden Steelworks, Inc.</h3>
    <p><svg viewBox="0 0 10 10"><path d="M5 0a3.5 3.5 0 0 0-3.5 3.5C1.5 6 5 10 5 10s3.5-4 3.5-6.5A3.5 3.5 0 0 0 5 0zm0 5a1.4 1.4 0 1 1 0-2.8A1.4 1.4 0 0 1 5 5z"/></svg>2740 Orchard Rd. Fairview, VA 23000</p>
    <p><svg viewBox="0 0 10 10"><path d="M2 0l2 2.5-1 1.2a6 6 0 0 0 3.3 3.3l1.2-1L10 8 8.5 10C4 9.5.5 6 0 1.5z"/></svg>(555)-310-2284</p>
    <p><svg viewBox="0 0 10 10"><circle cx="5" cy="5" r="5"/></svg>www.haldensteelworks.com</p>
  </div>

  <svg class="hexart" style="left:750px;top:375px" width="283" height="360" viewBox="0 0 283 360">
    <polygon points="180,0 283,58 283,360 40,360 0,335 0,100" fill="var(--royal)"/>
    <polygon points="180,18 283,76 283,360 52,360 18,338 18,110" fill="#6f7784" role="img" aria-label="Metal fabrication shop with a shear machine and workers"/>
  </svg>
</section>

</body>
</html>
```